Food company needs package designed to hold recipe cards.

We are a food manufacturer in Texas and we need a design for a small package that will hold 50 recipe cards. The end-product will be sold at retail stores across the USA. The package will be made from 24 pt cardstock. When package box is constructed and glued together, the measurements will be 5.25” x 0.9” x 4.25”.
We would like to see an eye-catching ARTISTIC design. The design does not necessarily need to include images of food to convey the message that recipes are included inside the box. However, if images of food are not included, text / copy will be needed to give details of the contents.
Target Market(s)
Cooks, Foodies, Chefs, Shoppers.
Industry/Entity Type
Food Manufacturer.
Requirements
Must have
- One or more of our logos. Contents included in the box; "Recipe Cards".
Should not have
- Bee graphics, honey dipper graphics. This project is about food, not bees or honey.

```html
<!DOCTYPE html>
<html lang="en">
<head>
<meta charset="utf-8">
<title>50 Recipes Cards – Box Dieline</title>
<link href="https://fonts.googleapis.com/css2?family=Cinzel:wght@400;500&family=Josefin+Sans:wght@600&display=swap" rel="stylesheet">
<style>
  :root {
    --bg: #575757;
    --paper: #ffffff;
    --teal: #22fdb6;
    --lime: #bbff00;
    --lime-dark: #ace600;
    --ink: #111111;
    --hatch: #9a9a9a;
  }
  html, body { margin: 0; padding: 0; overflow: hidden; }
  body { width: 1200px; height: 1200px; background: var(--bg); }
  .dieline { display: block; width: 1200px; height: 1200px; }
  .flap { fill: var(--paper); }
  .spine { fill: var(--teal); }
  .lime { fill: var(--lime); }
  .lime-band { fill: var(--lime-dark); }
  .label-box { fill: var(--paper); fill-opacity: 0.88; }
  .rule { stroke: var(--ink); stroke-width: 1.6; }
  .frame { fill: none; stroke: var(--ink); stroke-width: 1.6; }
  .spine-title { font-family: "Cinzel", serif; font-size: 36px; fill: var(--ink); }
  .body-copy { font-family: "Josefin Sans", sans-serif; font-weight: 600; font-size: 10.4px; fill: var(--ink); letter-spacing: 0.2px; }
  .title { font-family: "Cinzel", serif; fill: var(--ink); }
  .title-num { font-size: 70px; }
  .title-word { font-size: 74px; }
  .tagline { font-family: "Josefin Sans", sans-serif; font-weight: 600; font-size: 8px; fill: var(--ink); }
  .glue-hatch { stroke: var(--hatch); stroke-width: 1; }
</style>
</head>
<body>
<svg class="dieline" viewBox="0 0 1200 1200" xmlns="http://www.w3.org/2000/svg">
  <defs>
    <linearGradient id="artBack" x1="0" y1="0" x2="1" y2="1">
      <stop offset="0" stop-color="#e3ec3c"/>
      <stop offset="0.35" stop-color="#e6e6e6"/>
      <stop offset="0.6" stop-color="#d9e8a8"/>
      <stop offset="0.8" stop-color="#e9a23a"/>
      <stop offset="1" stop-color="#3ee6a4"/>
    </linearGradient>
    <linearGradient id="artFront" x1="0" y1="0" x2="1" y2="1">
      <stop offset="0" stop-color="#f2f05a"/>
      <stop offset="0.4" stop-color="#eeeeee"/>
      <stop offset="0.65" stop-color="#c7ef6a"/>
      <stop offset="0.85" stop-color="#efa226"/>
      <stop offset="1" stop-color="#28f0ae"/>
    </linearGradient>
    <clipPath id="glueClip"><polygon points="1118,422 1160,463 1160,754 1118,798"/></clipPath>
  </defs>

  <!-- left end flaps -->
  <polygon class="flap" points="30,353 90,353 108,392 108,422 30,422"/>
  <polygon class="flap" points="30,798 108,798 108,828 90,867 30,867"/>
  <rect class="spine" x="30" y="422" width="78" height="376"/>
  <text class="spine-title" transform="translate(78,610) rotate(-90)" text-anchor="middle">50 Recipes Cards</text>

  <!-- back panel -->
  <rect x="108" y="422" width="467" height="376" fill="url(#artBack)" role="img" aria-label="Hand-drawn food illustration pattern with colour blobs"/>
  <rect class="label-box" x="150" y="462" width="375" height="301"/>
  <line class="rule" x1="261" y1="535" x2="408" y2="535"/>
  <line class="rule" x1="261" y1="706" x2="408" y2="706"/>
  <text class="body-copy" text-anchor="middle">
    <tspan x="342" y="564">LOREM IPSUM DOLOR SIT AMET, CONSEC-</tspan>
    <tspan x="342" y="577">TETUER ADIPISCING ELIT, SED DIAM NONUM-</tspan>
    <tspan x="342" y="590">MY NIBH EUISMOD TINCIDUNT UT LAOREET</tspan>
    <tspan x="342" y="604">DOLORE MAGNA ALIQUAM ERAT VOLUTPAT.</tspan>
    <tspan x="342" y="617">UT WISI ENIM AD MINIM VENIAM, QUIS</tspan>
    <tspan x="342" y="630">NOSTRUD EXERCI TATION ULLAMCORPER</tspan>
    <tspan x="342" y="644">SUSCIPIT LOBORTIS NISL UT ALIQUIP EX EA</tspan>
    <tspan x="342" y="657">COMMODO CONSEQUAT. DUIS AUTEM VEL</tspan>
    <tspan x="342" y="670">EUM IRIURE DOLOR IN HENDRERIT IN VULPU-</tspan>
    <tspan x="342" y="684">TATE VELIT ESSE MOLESTIE CONSEQUAT, VEL</tspan>
  </text>

  <!-- middle spine -->
  <polygon class="flap" points="575,392 592,353 653,353 653,422 575,422"/>
  <polygon class="flap" points="575,798 653,798 653,867 592,867 575,828"/>
  <rect class="spine" x="575" y="422" width="78" height="376"/>
  <text class="spine-title" transform="translate(602,610) rotate(90)" text-anchor="middle">50 Recipes Cards</text>

  <!-- front lid flaps -->
  <path class="lime-band" d="M653,422 V305 Q653,285 673,285 H1098 Q1118,285 1118,305 V422 Z"/>
  <rect class="lime" x="653" y="344" width="465" height="78"/>
  <path class="lime-band" d="M653,798 V913 Q653,933 673,933 H1098 Q1118,933 1118,913 V798 Z"/>
  <rect class="lime" x="653" y="798" width="465" height="77"/>

  <!-- glue flap -->
  <polygon class="flap" points="1118,422 1160,463 1160,754 1118,798"/>
  <g clip-path="url(#glueClip)">
    <g class="glue-hatch">
      <line x1="1140" y1="480" x2="1160" y2="460"/><line x1="1140" y1="500" x2="1160" y2="480"/>
      <line x1="1140" y1="520" x2="1160" y2="500"/><line x1="1140" y1="540" x2="1160" y2="520"/>
      <line x1="1140" y1="560" x2="1160" y2="540"/><line x1="1140" y1="580" x2="1160" y2="560"/>
      <line x1="1140" y1="600" x2="1160" y2="580"/><line x1="1140" y1="620" x2="1160" y2="600"/>
      <line x1="1140" y1="640" x2="1160" y2="620"/><line x1="1140" y1="660" x2="1160" y2="640"/>
      <line x1="1140" y1="680" x2="1160" y2="660"/><line x1="1140" y1="700" x2="1160" y2="680"/>
      <line x1="1140" y1="720" x2="1160" y2="700"/><line x1="1140" y1="740" x2="1160" y2="720"/>
      <line x1="1140" y1="760" x2="1160" y2="740"/>
    </g>
  </g>

  <!-- front panel -->
  <rect x="653" y="422" width="465" height="376" fill="url(#artFront)" role="img" aria-label="Hand-drawn food illustration pattern with colour blobs"/>
  <rect class="label-box" x="693" y="461" width="378" height="303"/>
  <rect class="frame" x="707" y="479" width="350" height="267"/>
  <text class="title title-num" x="890" y="569" text-anchor="middle">50</text>
  <text class="title title-word" x="888" y="629" text-anchor="middle">Recipes</text>
  <text class="title title-word" x="885" y="688" text-anchor="middle">Cards</text>
  <text class="tagline" x="882" y="717" text-anchor="middle">EVERYDAY RECIPES FOR COOKING WITH HONEY</text>
</svg>
</body>
</html>
```